Brisbane IT support business needs our first business card

Hello we are a Brisbane based Information Technology company providing support and services to small and medium sized businesses. We provide a range of services and solutions.

The business name is Wattlebrook Network Computing Services, or WNCS for short.

I am looking for a business card that looks professional (don't we all want that), but most importantly, it most utilize the colours in the logo attached.

Reason: Launched late, extending so people have enough time to actually submit something.

Target Market(s)

Other business owners seeking our IT services, and also home users.

Industry/Entity Type

Business

Requirements
Must have
• Please only use the blue/orange colours in logo attached

```html
<!DOCTYPE html>
<html lang="en">
<head>
<meta charset="utf-8">
<title>WNCS Business Card</title>
<link rel="stylesheet" href="https://fonts.googleapis.com/css2?family=Open+Sans:wght@400;600;700&display=swap">
<style>
  :root {
    --navy: #17506b;
    --orange: #e8802e;
    --white: #ffffff;
    --backdrop: #222222;
    --card-w: 520px;
    --card-h: 297px;
  }
  * { box-sizing: border-box; margin: 0; padding: 0; }
  html, body {
    width: 1200px; height: 800px; overflow: hidden;
    background: var(--backdrop);
    font-family: "Open Sans", Arial, sans-serif;
  }
  .stage {
    width: 1200px; height: 800px;
    display: flex; align-items: center; justify-content: center; gap: 60px;
  }
  .card {
    position: relative;
    width: var(--card-w); height: var(--card-h);
    overflow: hidden;
    box-shadow: 0 10px 24px rgba(0,0,0,0.45);
  }

  /* Front */
  .card-front {
    background: var(--white);
    display: flex; flex-direction: column; align-items: center; justify-content: center;
  }
  .brand { display: flex; align-items: center; gap: 16px; }
  .brand-dot {
    width: 70px; height: 70px; border-radius: 50%;
    background: var(--navy);
  }
  .brand-name {
    font-weight: 700; font-size: 54px; letter-spacing: 1px;
    color: var(--orange); line-height: 1;
  }
  .front-tagline {
    margin-top: 26px;
    font-size: 19px; color: var(--navy); font-weight: 400;
  }

  /* Back */
  .card-back { background: var(--orange); }
  .back-band { position: absolute; inset: 0; }
  .contact {
    position: absolute; left: 40px; top: 78px;
    color: var(--white);
  }
  .contact-name { font-size: 16px; font-weight: 700; color: var(--navy); line-height: 1.1; }
  .contact-role { font-size: 12px; color: var(--navy); margin-bottom: 22px; }
  .contact-list { list-style: none; }
  .contact-item {
    display: flex; align-items: center; gap: 14px;
    font-size: 12px; height: 24px;
  }
  .contact-item svg { width: 12px; height: 12px; fill: var(--navy); flex: none; }
  .brand-panel {
    position: absolute; left: 290px; top: 118px;
    width: 210px; height: 120px;
    background: var(--white);
    display: flex; flex-direction: column; align-items: center; justify-content: center;
  }
  .brand-panel .brand { gap: 10px; }
  .brand-panel .brand-dot { width: 42px; height: 42px; }
  .brand-panel .brand-name { font-size: 32px; }
  .panel-tagline { margin-top: 12px; font-size: 10px; color: var(--navy); }
</style>
</head>
<body>
<main class="stage">
  <section class="card card-front">
    <div class="brand">
      <span class="brand-dot"></span>
      <span class="brand-name">WNCS</span>
    </div>
    <p class="front-tagline">Wattlebrook Network Computing Services</p>
  </section>

  <section class="card card-back">
    <svg class="back-band" viewBox="0 0 520 297" preserveAspectRatio="none" aria-hidden="true">
      <polygon points="418,0 458,0 198,297 158,297" fill="var(--navy)"/>
    </svg>

    <div class="contact">
      <p class="contact-name">Aaron Pell</p>
      <p class="contact-role">Manager</p>
      <ul class="contact-list">
        <li class="contact-item">
          <svg viewBox="0 0 24 24"><path d="M6.6 10.8a15 15 0 0 0 6.6 6.6l2.2-2.2a1 1 0 0 1 1-.25 11.4 11.4 0 0 0 3.6.57 1 1 0 0 1 1 1V20a1 1 0 0 1-1 1A17 17 0 0 1 3 4a1 1 0 0 1 1-1h3.5a1 1 0 0 1 1 1c0 1.25.2 2.45.57 3.57a1 1 0 0 1-.25 1z"/></svg>
          <span>00 987 654 321</span>
        </li>
        <li class="contact-item">
          <svg viewBox="0 0 24 24"><circle cx="12" cy="12" r="10"/><path d="M2 12h20M12 2c3 3 3 17 0 20M12 2c-3 3-3 17 0 20" stroke="var(--orange)" stroke-width="1.6" fill="none"/></svg>
          <span>www.wncs.example</span>
        </li>
        <li class="contact-item">
          <svg viewBox="0 0 24 24"><rect x="2" y="5" width="20" height="14" rx="1"/><path d="M2 6l10 7 10-7" stroke="var(--orange)" stroke-width="1.6" fill="none"/></svg>
          <span>contact@wncs.example</span>
        </li>
      </ul>
    </div>

    <div class="brand-panel">
      <div class="brand">
        <span class="brand-dot"></span>
        <span class="brand-name">WNCS</span>
      </div>
      <p class="panel-tagline">Wattlebrook Network Computing Services</p>
    </div>
  </section>
</main>
</body>
</html>
```